Business Card Design Project

Need business card for new non profit organization that includes the attached logo in some form.
with this information
Name: Michael Dorrance Pilbeam
Title: President & Founder
A: P.O. Box 51607, Portland, Oregon, 97214-5160
E: mike@dorrancetrust.org
E: mike@mikepilbeam.com
P: 1.971.555.0172

Industry/Entity Type
Non Profit

```html
<!DOCTYPE html>
<html lang="en">
<head>
<meta charset="utf-8">
<title>Dorrance Trust — Business Card</title>
<link rel="stylesheet" href="https://fonts.googleapis.com/css2?family=Lato:wght@300;400;700&display=swap">
<style>
  :root {
    --navy: #27306b;
    --navy-deep: #1c2352;
    --navy-soft: #3a4488;
    --ink: #161823;
    --card-light: #f6f6f7;
    --card-shade: #e4e5e8;
    --backdrop: #e9e9ea;
  }
  * { box-sizing: border-box; margin: 0; padding: 0; }
  html, body {
    width: 1200px; height: 900px; overflow: hidden;
    background: var(--backdrop);
    font-family: "Lato", Arial, sans-serif;
  }
  .card {
    position: absolute; left: 100px; top: 164px;
    width: 1000px; height: 572px;
    background: linear-gradient(160deg, var(--card-light) 0%, var(--card-shade) 100%);
    overflow: hidden;
    box-shadow: 0 10px 30px rgba(0,0,0,0.18);
  }
  .side-panel { position: absolute; left: 660px; top: 0; width: 340px; height: 572px; }
  .brand {
    position: absolute; left: 210px; top: 60px;
    display: flex; align-items: center; gap: 16px;
    color: var(--navy);
    font-weight: 700; font-size: 34px; letter-spacing: 0.5px;
  }
  .brand-dot { width: 30px; height: 30px; border-radius: 50%; background: var(--navy); }
  .name-marker {
    position: absolute; left: 0; top: 190px;
    width: 92px; height: 50px;
    background: linear-gradient(135deg, var(--navy-soft), var(--navy));
  }
  .name-block {
    position: absolute; left: 106px; top: 192px;
    display: inline-flex; flex-direction: column; align-items: flex-end;
  }
  .name {
    font-weight: 400; font-size: 44px; color: var(--ink); white-space: nowrap;
    line-height: 1;
  }
  .title {
    margin-top: 6px;
    font-size: 15px; color: var(--navy-soft); white-space: nowrap;
  }
  .contacts {
    position: absolute; left: 98px; top: 378px;
    list-style: none; font-size: 17px; color: var(--ink);
  }
  .contacts li { display: flex; align-items: center; gap: 10px; height: 26px; }
  .contacts svg { width: 15px; height: 15px; fill: var(--navy); flex: none; }
</style>
</head>
<body>
  <div class="card">
    <svg class="side-panel" viewBox="0 0 340 572" aria-hidden="true">
      <rect width="340" height="572" fill="#27306b"/>
      <polygon points="0,0 340,0 340,260 0,110" fill="#2e3878"/>
      <polygon points="60,0 340,0 340,150" fill="#343f82" opacity="0.7"/>
      <polygon points="0,300 340,200 340,572 0,572" fill="#1c2352" opacity="0.6"/>
      <polygon points="120,572 340,380 340,572" fill="#161c45" opacity="0.7"/>
    </svg>

    <div class="brand"><span class="brand-dot"></span>Dorrance Trust</div>

    <div class="name-marker"></div>
    <div class="name-block">
      <h1 class="name">Michael Dorrance Pilbeam</h1>
      <p class="title">President &amp; Founder</p>
    </div>

    <ul class="contacts">
      <li><svg viewBox="0 0 16 16"><path d="M3 1h3l1 4-2 1a9 9 0 0 0 5 5l1-2 4 1v3a2 2 0 0 1-2 2A13 13 0 0 1 1 3a2 2 0 0 1 2-2z"/></svg>1.971.555.0172</li>
      <li><svg viewBox="0 0 16 16"><path d="M1 3h14v10H1zM2.5 4.5v.3L8 8.5l5.5-3.7v-.3zM2.5 6.6v5h11v-5L8 10.3z"/></svg>mike@mikepilbeam.com</li>
      <li><svg viewBox="0 0 16 16"><path d="M1 3h14v10H1zM2.5 4.5v.3L8 8.5l5.5-3.7v-.3zM2.5 6.6v5h11v-5L8 10.3z"/></svg>mike@dorrancetrust.org</li>
      <li><svg viewBox="0 0 16 16"><path d="M8 0a5 5 0 0 1 5 5c0 4-5 11-5 11S3 9 3 5a5 5 0 0 1 5-5zm0 3a2 2 0 1 0 0 4 2 2 0 0 0 0-4z"/></svg>P.O. Box 51607, Portland, Oregon, 97214-5160</li>
    </ul>
  </div>
</body>
</html>
```